Packaging design for Vorlo Toss Style snack

Looking for food product packaging. Our product is a sweet, salty, and savory vorlo toss style snack. We would like to see designs that use the colors yellow and red and any color that compliments them is welcomed. Preferably pastel if possible to be more modern contemporary but with an appeal to kids to young adults. The final design should communicate spark curiosity, hunger, and addiction.

Target Market(s)

12 - 60 year olds. Mainly targeting younger kids but also to older adults

Industry/Entity Type

Food & Beverage

Colors
FFF300
FFF600
FEFA6F
FFFEC7
FFFEE8
FFC000
F8CF3A
FAE287
FDF2CF
FEFAEE
F0912C
F2A743
F7CA91
FBE8D2
FDF5EE
EE7325
F08F49
F5BC92
FAE3D3
FDF4ED

```html
<!DOCTYPE html>
<html lang="en">
<head>
<meta charset="utf-8">
<title>Crunzo Bites – Cereal Mix Pouch</title>
<link rel="stylesheet" href="https://fonts.googleapis.com/css2?family=Fredoka:wght@700&family=Montserrat:wght@500;700;800&family=Open+Sans:wght@400&display=swap">
<style>
  :root {
    --page: #ffffff;
    --lemon: #fff300;
    --lemon-deep: #e8d800;
    --gold: #ffc000;
    --orange: #f0912c;
    --orange-deep: #ee7325;
    --ember: #d9521c;
    --red: #d40f1c;
    --ink: #111111;
    --cream: #fdf2cf;
  }
  * { margin: 0; padding: 0; box-sizing: border-box; }
  html, body { width: 1200px; height: 900px; overflow: hidden; background: var(--page); }
  .canvas { position: relative; width: 1200px; height: 900px; background: var(--page); }
  .pouch {
    position: absolute; left: 380px; top: 141px; width: 436px; height: 650px;
    border-radius: 14px 14px 4px 4px; overflow: hidden;
    background: linear-gradient(180deg, var(--lemon) 0%, var(--lemon-deep) 100%);
  }
  .pouch-art { position: absolute; inset: 0; }
  .brand {
    position: absolute; left: 134px; width: 160px; top: 116px; text-align: center;
    font-family: "Montserrat", sans-serif; font-weight: 800; font-size: 34px;
    color: var(--red); letter-spacing: -0.5px; line-height: 38px;
  }
  .tagline {
    position: absolute; left: 0; width: 436px; top: 203px; text-align: center;
    font-family: "Montserrat", sans-serif; font-weight: 500; font-size: 10.5px;
    color: var(--ink); letter-spacing: 0.3px; line-height: 13px; white-space: nowrap;
  }
  .product-name {
    position: absolute; left: 87px; width: 262px; top: 303px; text-align: center;
    font-family: "Fredoka", sans-serif; font-weight: 700; line-height: 0.95;
  }
  .product-name .line-cereal { display: block; font-size: 44px; color: var(--ink); letter-spacing: 1px; }
  .product-name .line-mix { display: block; font-size: 92px; color: var(--red); margin-top: 2px; }
  .blurb {
    position: absolute; left: 30px; width: 204px; top: 544px; text-align: center;
    font-family: "Open Sans", sans-serif; font-size: 11.5px; line-height: 15px;
    color: var(--cream); white-space: nowrap;
  }
  .net-weight {
    position: absolute; left: 70px; top: 611px; width: 104px; height: 39px;
    background: var(--lemon); border-radius: 8px 8px 0 0;
    font-family: "Montserrat", sans-serif; font-weight: 800; font-style: italic;
    font-size: 18px; color: var(--ink); text-align: center; line-height: 39px;
  }
</style>
</head>
<body>
<div class="canvas">
  <div class="pouch">
    <svg class="pouch-art" width="436" height="650" viewBox="0 0 436 650">
      <defs>
        <linearGradient id="orangeBand" x1="0" y1="0" x2="0" y2="1">
          <stop offset="0" stop-color="#f2a743"/>
          <stop offset="1" stop-color="#ee7325"/>
        </linearGradient>
        <linearGradient id="snackFill" x1="0" y1="0" x2="1" y2="1">
          <stop offset="0" stop-color="#c9a27a"/>
          <stop offset="0.5" stop-color="#8a5e38"/>
          <stop offset="1" stop-color="#5a3a22"/>
        </linearGradient>
      </defs>
      <rect class="seal-strip" x="18" y="6" width="400" height="16" fill="#ffc000" opacity="0.55"/>
      <rect class="zipper-line" x="18" y="74" width="400" height="6" rx="3" fill="#fff600"/>
      <polygon class="lower-band" points="0,358 436,257 436,650 0,650" fill="url(#orangeBand)"/>
      <polygon class="product-window" role="img" aria-label="Photo of the cereal snack mix: square cereal pieces, crackers and chips"
        points="356,355 422,365 422,650 335,650 220,507" fill="url(#snackFill)"/>
      <circle class="badge-fill" cx="218" cy="366" r="122" fill="#fff300"/>
      <circle class="badge-ring" cx="218" cy="366" r="128" fill="none" stroke="#d9521c" stroke-width="9"/>
    </svg>
    <div class="brand">Crunzo<br>Bites</div>
    <div class="tagline">HOOKED ON EVERY CRUNCH</div>
    <div class="product-name">
      <span class="line-cereal">CEREAL</span>
      <span class="line-mix">Mix</span>
    </div>
    <p class="blurb">Lorem Ipsum is simply dummy<br>text of the printing and typesetting<br>industry. Lorem Ipsum has been the<br>industry's standard dummy</p>
    <div class="net-weight">250gm</div>
  </div>
</div>
</body>
</html>
```